Calm Fern Wellcare- Aged Care and Community Services

Looking for brochure to advertise our services. I will attach a draft that we do not want to use. Looking for graphics that are as natural as possible to present a personalised service. We supply services to aged people and people with disability. Please make it look classy and professional at the same time. I am looking for creativity. I have also attached the logo. Site addresses can be the last page. ideally looking for 2 designs, one A4 and another smaller possibly DL. Looking for creative out of the box thinkers. Thank you.

Target Market(s)

Aged Care service providers, disability service providers and private hospitals

Font styles to use
Serif
Sans Serif
Script

Colors
6b449b
886aae
eea4c8
f59195
fac994
3176b5
0555a3
cedeed
e4daeb

Requirements
Must have
• Targeted imagery, content and contact details
Nice to have
• personal profiles of people happy with our services

```html
<!DOCTYPE html>
<html lang="en">
<head>
<meta charset="utf-8">
<title>Calm Fern Wellcare – Brochure A4 and DL</title>
<link rel="stylesheet" href="https://fonts.googleapis.com/css2?family=Roboto:wght@300;400;500;700;900&display=swap">
<style>
:root{
  --purple:#6b449b;
  --purple-mid:#886aae;
  --lavender:#e4daeb;
  --ink:#1d1d1d;
  --star:#f7b500;
  --searchly:#3d6fc4;
  --white:#ffffff;
  --shadow:0 2px 5px rgba(0,0,0,.3);
}
*{margin:0;padding:0;box-sizing:border-box}
html,body{width:1200px;height:865px;overflow:hidden;background:var(--white)}
body{position:relative;font-family:"Roboto",Arial,sans-serif;color:var(--ink)}
.panel{position:absolute;background:var(--white);overflow:hidden;box-shadow:var(--shadow)}
.panel svg.layer{position:absolute;left:0;top:0}
.abs{position:absolute}
.label{position:absolute;font-size:30px;font-weight:400;color:#000;letter-spacing:.5px}
.brand{position:absolute;color:var(--purple);font-weight:500;display:flex;align-items:center;gap:3px;white-space:nowrap}
.brand .dot{display:inline-block;border-radius:50%;background:var(--purple)}
.heading{position:absolute;color:var(--purple);font-weight:500;white-space:nowrap}
.body-text{position:absolute;line-height:1.12}
.body-text p+p{margin-top:1em}
.badge{position:absolute;border-radius:50%;background:var(--purple);border:2px solid var(--white);box-shadow:0 0 0 1px var(--purple-mid);color:var(--white);text-align:center;display:flex;flex-direction:column;justify-content:center;line-height:1}
.badge b{font-weight:900}
.stars{position:absolute;color:var(--star);letter-spacing:2px;text-align:center}
.search-bar{position:absolute;border:1px solid #bbb;border-radius:6px;display:flex;align-items:center;padding-left:4px;color:#222;background:var(--white)}
.review{position:absolute;color:var(--white);text-align:center}
.review .card{position:absolute;left:0;right:0;bottom:0;background:var(--purple)}
.review .circle{position:absolute;left:50%;transform:translateX(-50%);border-radius:50%;background:var(--purple);border:1.5px solid var(--white);display:flex;flex-direction:column;align-items:center;justify-content:center;font-weight:700;line-height:1.05}
.review .circle .s{color:var(--star);font-weight:400;letter-spacing:.5px}
.review .quote{position:absolute;left:3px;right:3px;line-height:1.2;font-weight:300}
.value-list{position:absolute;list-style:none}
.value-list li{position:relative;line-height:1.05}
.value-list li::before{content:"";position:absolute;background:var(--purple)}
.a4-why .value-list li::before{left:-10px;top:0;width:5px;height:5px}
.dl-back .value-list li::before{left:-4px;top:0;width:2px;height:2px}
.service-list{position:absolute;list-style:none}
.service-list li{position:relative;line-height:1.45}
.service-list li::before{content:"+";position:absolute;color:var(--purple);font-weight:700}
.a4-service .service-list li::before{left:-8px;top:0}
.dl-front .service-list li::before{left:-4px;top:0}
.call{position:absolute;color:var(--white)}
.call .title{font-weight:900;line-height:1}
.call .phone{font-weight:400;line-height:1.1;white-space:nowrap}
.call .addr{display:flex;align-items:center;gap:2px;white-space:nowrap}
.email{position:absolute;color:var(--white);display:flex;align-items:center;white-space:nowrap}
</style>
</head>
<body>

<!-- A4 front -->
<section class="panel a4-front" style="left:88px;top:43px;width:261px;height:370px">
  <svg class="layer" width="261" height="370" aria-hidden="true">
    <defs>
      <linearGradient id="warm" x1="0" y1="0" x2="1" y2="1">
        <stop offset="0" stop-color="#cfc2b0"/><stop offset=".5" stop-color="#b99a7c"/><stop offset="1" stop-color="#8e6b52"/>
      </linearGradient>
    </defs>
    <circle cx="20" cy="398" r="135" fill="var(--lavender)"/>
    <circle cx="175" cy="42" r="173" fill="none" stroke="var(--purple-mid)" stroke-width="1"/>
    <circle cx="175" cy="40" r="167" fill="url(#warm)" stroke="var(--purple)" stroke-width="4"/>
  </svg>
  <div class="abs" role="img" aria-label="Photo of a smiling elderly woman with a carer holding her hand" style="left:10px;top:0;width:251px;height:205px"></div>
  <div class="brand" style="left:22px;top:34px;font-size:9px"><span class="dot" style="width:6px;height:6px"></span>Calm Fern Wellcare</div>
  <div class="badge" style="left:33px;top:143px;width:56px;height:56px;font-size:8px"><span>Because</span><b style="font-size:11px">we care</b></div>
  <h2 class="heading" style="left:16px;top:208px;font-size:12.5px;text-decoration:underline;text-underline-offset:2px">About us</h2>
  <div class="body-text" style="left:16px;top:233px;width:230px;font-size:6.4px">
    <p>Calm Fern Wellcare has a client focused approach which ensures it identifies individual client requirements to facilitate for a unique partnership without ambiguity. Our approach focuses on key pain areas of our clients which go beyond staffing needs. We ensure we look at the profile of the clients in your care to identify similar values and develop a “team based” system to ensure you always receive the same staff that meet your needs when you book your shifts.</p>
    <p>Our staff retention programs focus on the key drivers for staff to perform the work they do and whether their values are aligned to supporting vulnerable groups in society. With a proactive reward and recognition program, Calm Fern are well informed of areas of improvement to retain the very best talent. We believe our staff are a pillar to what we do, which is why we take every step to ensure they feel part of the great achievement and reward brought by supporting people who need assistance.</p>
  </div>
</section>

<!-- A4 back -->
<section class="panel a4-back" style="left:367px;top:43px;width:261px;height:370px">
  <svg class="layer" width="261" height="370" aria-hidden="true">
    <ellipse cx="-10" cy="385" rx="127" ry="120" fill="var(--purple)" stroke="var(--lavender)" stroke-width="3"/>
    <path d="M92,370 L92,354 Q96,348 112,348 L238,348 Q258,348 261,362 L261,370 Z" fill="var(--purple)"/>
  </svg>
  <p class="heading" style="left:0;width:261px;top:18px;text-align:center;font-size:12.5px;font-weight:400">Hear what our client are saying on</p>
  <p class="heading" style="left:0;width:261px;top:38px;text-align:center;font-size:28px;font-weight:400;color:var(--searchly)">Searchly</p>
  <div class="search-bar" style="left:75px;top:75px;width:111px;height:9px;font-size:5.5px">⌕&nbsp;Calm Fern Wellcare</div>
  <div class="stars" style="left:0;width:261px;top:89px;font-size:17px">★★★★★</div>
  <div class="review" style="left:9px;top:118px;width:57px;height:80px">
    <div class="card" style="top:24px"></div>
    <div class="circle" style="top:0;width:48px;height:48px;font-size:5.3px">Amira Chol<span class="s">★★★★★</span></div>
    <p class="quote" style="top:52px;font-size:4.2px;text-align:left">Provides flexibility to all the staffs, highly recommended, love everything about Calm Fern.</p>
  </div>
  <div class="review" style="left:71px;top:118px;width:57px;height:80px">
    <div class="card" style="top:24px"></div>
    <div class="circle" style="top:0;width:48px;height:48px;font-size:5.3px">Clare Ann<span class="s">★★★★★</span></div>
    <p class="quote" style="top:52px;font-size:4.2px;text-align:left">One of the best agency in WA. Highly recommended</p>
  </div>
  <div class="review" style="left:133px;top:118px;width:57px;height:80px">
    <div class="card" style="top:24px"></div>
    <div class="circle" style="top:0;width:48px;height:48px;font-size:5.3px">Felicity Zane<span class="s">★★★★★</span></div>
    <p class="quote" style="top:54px;font-size:4.2px">Professionalism, Responsiveness</p>
  </div>
  <div class="review" style="left:194px;top:118px;width:57px;height:80px">
    <div class="card" style="top:24px"></div>
    <div class="circle" style="top:0;width:48px;height:48px;font-size:5.3px">Zara Khan<span class="s">★★★★★</span></div>
    <p class="quote" style="top:52px;font-size:4.2px;text-align:left">They provides flexibility to each other with highly trained highly recommended team</p>
  </div>
  <div class="brand" style="left:0;width:261px;justify-content:center;top:244px;font-size:12px"><span class="dot" style="width:8px;height:8px"></span>Calm Fern Wellcare</div>
  <div class="call" style="left:14px;top:301px">
    <p class="title" style="font-size:18px">Call us</p>
    <p class="phone" style="font-size:12.5px;margin-left:-4px">08 9000 4127</p>
    <p class="addr" style="font-size:5.2px;margin-left:-4px;margin-top:1px"><svg width="5" height="6" viewBox="0 0 10 12" aria-hidden="true"><path d="M5 0a4 4 0 0 1 4 4c0 3-4 8-4 8S1 7 1 4a4 4 0 0 1 4-4z" fill="#fff"/></svg>14 Willow Lane, Southvale WA 6000</p>
  </div>
  <div class="email" style="left:110px;top:353px;font-size:6.3px;gap:6px">
    <svg width="15" height="10" viewBox="0 0 15 10" aria-hidden="true"><rect x=".5" y=".5" width="14" height="9" fill="none" stroke="#fff"/><path d="M.5 .5 7.5 6 14.5 .5" fill="none" stroke="#fff"/></svg>
    admin@calmfernwellcare.com.au
  </div>
</section>

<!-- A4 inside: why choose us -->
<section class="panel a4-why" style="left:646px;top:43px;width:261px;height:370px">
  <h2 class="heading" style="left:11px;top:10px;font-size:13px">WHY CHOOSE US?</h2>
  <div class="body-text" style="left:11px;top:31px;width:240px;font-size:6.2px">
    <p>Calm Fern Wellcare partners with likeminded organisations with a passion for making a difference to the lives of the vulnerable. We have differentiated ourselves by redefining the model of traditional staffing agencies and developed an obsessive desire to meet our clients needs. We genuinely care about what we do and know the impact under resourcing can do to day to day service delivery and overall quality outcomes.</p>
    <p>If you partner with us, we guarantee a tailored approach to meeting your needs.</p>
  </div>
  <h2 class="heading" style="left:10px;top:101px;font-size:13px">OUR VALUE PROPOSITION</h2>
  <ul class="value-list" style="left:21px;top:122px;width:225px;font-size:6.2px">
    <li style="margin-bottom:7px">Our people are individually selected and participate in robust recruitment processes</li>
    <li style="margin-bottom:7px">We treat everyone with respect and believe our staff are the purpose of our existence</li>
    <li style="margin-bottom:7px">We are responsive to our clients priorities and walk along their journey to achieving operational excellence</li>
    <li style="margin-bottom:7px">We believe in ethical practices, transparency, and accountability</li>
    <li style="margin-bottom:6px">We are deliberate in our approach and have a passion for human services</li>
    <li>We have a ‘bias for action’ and unceasingly pursue opportunities to change and adapt to the needs of our clients and environment</li>
  </ul>
  <svg class="layer" width="261" height="370" aria-hidden="true">
    <defs>
      <linearGradient id="garden" x1="0" y1="0" x2="1" y2="1">
        <stop offset="0" stop-color="#6f9a5a"/><stop offset=".5" stop-color="#c9b18f"/><stop offset="1" stop-color="#8b6a55"/>
      </linearGradient>
    </defs>
    <path d="M0,271 Q120,195 261,285" fill="none" stroke="var(--purple-mid)" stroke-width="1"/>
    <path d="M0,276 Q120,202 261,290 L261,370 L0,370 Z" fill="url(#garden)" stroke="var(--purple)" stroke-width="3"/>
  </svg>
  <div class="abs" role="img" aria-label="Photo of elderly residents playing cards on a garden terrace with a carer" style="left:0;top:232px;width:261px;height:138px"></div>
</section>

<!-- A4 inside: our service -->
<section class="panel a4-service" style="left:924px;top:43px;width:261px;height:370px">
  <svg class="layer" width="261" height="370" aria-hidden="true">
    <defs>
      <linearGradient id="team" x1="0" y1="0" x2="1" y2="0">
        <stop offset="0" stop-color="#6b4a3a"/><stop offset=".5" stop-color="#c7a58c"/><stop offset="1" stop-color="#7b5a48"/>
      </linearGradient>
    </defs>
    <path d="M0,0 H261 V8 Q261,36 230,36 H30 Q8,36 0,20 Z" fill="var(--purple)"/>
    <rect x="0" y="232" width="261" height="138" fill="url(#team)"/>
    <path d="M40,370 Q180,350 261,300 L261,370 Z" fill="var(--purple)"/>
    <circle cx="48" cy="325" r="38" fill="var(--white)" stroke="var(--purple)" stroke-width="4"/>
  </svg>
  <div class="abs" role="img" aria-label="Photo of a diverse group of smiling care staff" style="left:0;top:232px;width:261px;height:138px"></div>
  <h2 class="abs" style="left:0;width:261px;top:4px;text-align:center;color:var(--white);font-size:25px;font-weight:300;line-height:1.1">OUR <b style="font-weight:700">SERVICE</b></h2>
  <div class="body-text" style="left:22px;top:45px;width:232px;font-size:6.3px">
    <p>Our mission is to supply values driven, responsive, conscientious, and responsible personnel to the aged care sector, disability services, private and public health sectors. Our passion for human services and experience in recruitment, enables us to attract exceptional people with great values ready and willing to make a difference to the lives of vulnerable people.</p>
    <p>We have a comprehensive database of the following personnel</p>
  </div>
  <ul class="service-list" style="left:38px;top:104px;width:215px;font-size:6.3px">
    <li>Registered Nurses (Aged Care, Disability, Emergency, Public and Private healthcare)</li>
    <li>Clinical Nurses</li>
    <li>Nurse Practitioners</li>
    <li>Enrolled Nurses</li>
    <li>Assistants in Nursing (Carers/ PCA’s)</li>
    <li>Support Workers (Disability, Community and Mental health)</li>
    <li>Healthcare Endorsed Chefs and Cooks</li>
    <li>Catering Assistants</li>
    <li>Kitchen hands</li>
    <li>Cleaners</li>
  </ul>
  <div class="brand" style="left:14px;top:320px;font-size:7px;width:68px;justify-content:center;white-space:normal;text-align:center;line-height:1.1">Calm Fern Wellcare</div>
</section>

<p class="label" style="left:158px;top:413px">FRONT</p>
<p class="label" style="left:465px;top:413px">BACK</p>

<!-- DL front -->
<section class="panel dl-front" style="left:443px;top:504px;width:124px;height:260px">
  <svg class="layer" width="124" height="260" aria-hidden="true">
    <defs>
      <linearGradient id="warm2" x1="0" y1="0" x2="1" y2="1">
        <stop offset="0" stop-color="#cfc2b0"/><stop offset=".5" stop-color="#b99a7c"/><stop offset="1" stop-color="#8e6b52"/>
      </linearGradient>
    </defs>
    <circle cx="104" cy="280" r="36" fill="var(--lavender)"/>
    <circle cx="86" cy="12" r="87" fill="url(#warm2)" stroke="var(--purple)" stroke-width="2.5"/>
  </svg>
  <div class="abs" role="img" aria-label="Photo of a smiling elderly woman with a carer" style="left:4px;top:0;width:120px;height:96px"></div>
  <div class="brand" style="left:12px;top:18px;font-size:4.5px"><span class="dot" style="width:3px;height:3px"></span>Calm Fern Wellcare</div>
  <div class="badge" style="left:15px;top:65px;width:27px;height:27px;font-size:4px;border-width:1px"><span>Because</span><b style="font-size:5px">we care</b></div>
  <h2 class="heading" style="left:8px;top:96px;font-size:6px;text-decoration:underline">About us</h2>
  <div class="body-text" style="left:8px;top:107px;width:108px;font-size:2.9px">
    <p>Calm Fern Wellcare has a client focused approach which ensures it identifies individual client requirements to facilitate for a unique partnership without ambiguity. Our approach focuses on key pain areas of our clients which go beyond staffing needs. We ensure we look at the profile of the clients in your care to identify similar values and develop a “team based” system to ensure you always receive the same staff that meet your needs when you book your shifts.</p>
    <p>Our staff retention programs focus on the key drivers for staff to perform the work they do and whether their values are aligned to supporting vulnerable groups in society. With a proactive reward and recognition program, Calm Fern are well informed of areas of improvement to retain the very best talent. We believe our staff are a pillar to what we do, which is why we take every step to ensure they feel part of the great achievement and reward brought by supporting people who need assistance.</p>
  </div>
  <h2 class="abs" style="left:19px;top:173px;font-size:11px;font-weight:300;color:var(--purple)">OUR <b style="font-weight:700">SERVICE</b></h2>
  <ul class="service-list" style="left:23px;top:193px;width:85px;font-size:2.8px">
    <li>Registered Nurses (Aged Care, Disability, Emergency, Public and Private healthcare)</li>
    <li>Clinical Nurses</li>
    <li>Nurse Practitioners</li>
    <li>Enrolled Nurses</li>
    <li>Assistants in Nursing (Carers/ PCA’s)</li>
    <li>Support Workers (Disability, Community and Mental health)</li>
    <li>Healthcare Endorsed Chefs and Cooks</li>
    <li>Catering Assistants</li>
    <li>Kitchen hands</li>
    <li>Cleaners</li>
  </ul>
</section>

<!-- DL back -->
<section class="panel dl-back" style="left:633px;top:504px;width:123px;height:260px">
  <svg class="layer" width="123" height="260" aria-hidden="true">
    <ellipse cx="-5" cy="262" rx="60" ry="52" fill="var(--purple)" stroke="var(--lavender)" stroke-width="1.5"/>
    <path d="M44,260 L44,252 Q46,249 54,249 L112,249 Q122,249 123,256 L123,260 Z" fill="var(--purple)"/>
  </svg>
  <h2 class="heading" style="left:5px;top:4px;font-size:5.5px">WHY CHOOSE US?</h2>
  <div class="body-text" style="left:5px;top:14px;width:113px;font-size:2.7px">
    <p>Calm Fern Wellcare partners with likeminded organisations with a passion for making a difference to the lives of the vulnerable. We have differentiated ourselves by redefining the model of traditional staffing agencies and developed an obsessive desire to meet our clients needs. We genuinely care about what we do and know the impact under resourcing can do to day to day service delivery and overall quality outcomes.</p>
    <p>If you partner with us, we guarantee a tailored approach to meeting your needs.</p>
  </div>
  <h2 class="heading" style="left:5px;top:48px;font-size:5.5px">OUR VALUE PROPOSITION</h2>
  <ul class="value-list" style="left:10px;top:57px;width:108px;font-size:2.6px">
    <li style="margin-bottom:3px">Our people are individually selected and participate in robust recruitment processes</li>
    <li style="margin-bottom:3px">We treat everyone with respect and believe our staff are the purpose of our existence</li>
    <li style="margin-bottom:3px">We are responsive to our clients priorities and walk along their journey to achieving operational excellence</li>
    <li style="margin-bottom:3px">We believe in ethical practices, transparency, and accountability</li>
    <li style="margin-bottom:3px">We are deliberate in our approach and have a passion for human services</li>
    <li>We have a ‘bias for action’ and unceasingly pursue opportunities to change and adapt to the needs of our clients and environment</li>
  </ul>
  <p class="heading" style="left:0;width:123px;top:104px;text-align:center;font-size:12px;font-weight:400;color:var(--searchly)">Searchly</p>
  <div class="search-bar" style="left:36px;top:121px;width:52px;height:5px;font-size:2.5px;border-radius:3px">Calm Fern Wellcare</div>
  <div class="stars" style="left:0;width:123px;top:127px;font-size:7px;letter-spacing:1px">★★★★★</div>
  <div class="review" style="left:5px;top:141px;width:26px;height:38px">
    <div class="card" style="top:11px"></div>
    <div class="circle" style="top:0;width:22px;height:22px;font-size:2.3px;border-width:.8px">Amira Chol<span class="s">★★★★★</span></div>
    <p class="quote" style="top:24px;font-size:2px;left:1px;right:1px;text-align:left">Provides flexibility to all the staffs, highly recommended</p>
  </div>
  <div class="review" style="left:34px;top:141px;width:26px;height:38px">
    <div class="card" style="top:11px"></div>
    <div class="circle" style="top:0;width:22px;height:22px;font-size:2.3px;border-width:.8px">Clare Ann<span class="s">★★★★★</span></div>
    <p class="quote" style="top:24px;font-size:2px;left:1px;right:1px;text-align:left">One of the best agency in WA. Highly recommended</p>
  </div>
  <div class="review" style="left:63px;top:141px;width:26px;height:38px">
    <div class="card" style="top:11px"></div>
    <div class="circle" style="top:0;width:22px;height:22px;font-size:2.3px;border-width:.8px">Felicity Zane<span class="s">★★★★★</span></div>
    <p class="quote" style="top:25px;font-size:2px">Professionalism, Responsiveness</p>
  </div>
  <div class="review" style="left:92px;top:141px;width:26px;height:38px">
    <div class="card" style="top:11px"></div>
    <div class="circle" style="top:0;width:22px;height:22px;font-size:2.3px;border-width:.8px">Zara Khan<span class="s">★★★★★</span></div>
    <p class="quote" style="top:24px;font-size:2px;left:1px;right:1px;text-align:left">They provides flexibility, highly trained team</p>
  </div>
  <p class="heading" style="left:0;width:123px;top:181px;text-align:center;font-size:5.3px;font-weight:400">Hear what our client are saying on <b style="font-weight:700">Searchly</b></p>
  <div class="brand" style="left:0;width:123px;justify-content:center;top:200px;font-size:6px"><span class="dot" style="width:4px;height:4px"></span>Calm Fern Wellcare</div>
  <div class="call" style="left:6px;top:227px">
    <p class="title" style="font-size:7.5px">Call us</p>
    <p class="phone" style="font-size:6px;margin-left:-2px">08 9000 4127</p>
    <p class="addr" style="font-size:2.3px;margin-left:-2px">14 Willow Lane, Southvale WA 6000</p>
  </div>
  <div class="email" style="left:52px;top:252px;font-size:2.8px;gap:3px">
    <svg width="7" height="5" viewBox="0 0 15 10" aria-hidden="true"><rect x=".5" y=".5" width="14" height="9" fill="#fff"/></svg>
    admin@calmfernwellcare.com.au
  </div>
</section>

<p class="label" style="left:583px;top:803px">DL</p>

</body>
</html>
```